Recto Verso Audiology Business Card

Business card with a beautiful design on the back. On the Recto you need the following data Dorvalle Ansel Audiologist Hearing Solutions Hearing Protection Tinnitus Hyperacusis Tel: 0481/27 53 09 Email: On the back, you need something nice like the attached file. The logo "Sola Brisa" can be in the center The colors of the Logo can not be changed If possible stay in the same colors as the logo Another solution is to put the logo on the front and have a nice back (A mosaic of small ears, hearing aids or other ..) Thank you _______________________________________________________________ Visit card On the Recto Dorvalle Ansel Audiologist Hearing Solutions Hearing Protection Tinnitus Hyperacusis Tel: 0481/27 53 09 Email: You can put the logo " Sola Brisa "on the Recto of the Verso The colors of the logo can not be changed. If you put the logo on the back, it must be well integrated. On the Verso I need something in the files. something stylish. It's a visit card for an audiologist. You can get ears of hearing aids if you need. Thanks

Target Market(s)

customers

Contact Information for Business Card

Carte de visite standard ou A6

Font styles to use
Serif
Sans Serif

Colors
33a6d7

Requirements
Must have
• the logo and a stylized background.
Nice to have
• It would be nice to have a back side related to audiology (ears, hearing aids etc.)

```html
<!DOCTYPE html>
<html lang="fr">
<head>
<meta charset="utf-8">
<title>Carte de visite – Dorvalle Ansel, Audiologue</title>
<link rel="stylesheet" href="https://fonts.googleapis.com/css2?family=Oswald:wght@400&family=Lato:wght@400&display=swap">
<style>
  :root {
    --page-bg: #e9e7e5;
    --card-light: #f6f4f4;
    --card-dark: #263a4d;
    --accent: #33a6d7;
    --text-light: #ffffff;
  }
  * { box-sizing: border-box; margin: 0; padding: 0; }
  html, body {
    width: 1200px;
    height: 900px;
    overflow: hidden;
    background: var(--page-bg);
  }
  .canvas {
    position: relative;
    width: 1200px;
    height: 900px;
  }
  .card {
    position: absolute;
    left: 274px;
    top: 248px;
    width: 652px;
    height: 404px;
    display: flex;
    box-shadow: 0 6px 22px rgba(0, 0, 0, 0.12);
  }
  .card__brand-side {
    width: 320px;
    background: var(--card-light);
    display: flex;
    align-items: center;
    justify-content: center;
  }
  .brand-name {
    font-family: "Oswald", sans-serif;
    font-weight: 400;
    font-size: 30px;
    letter-spacing: 2px;
    text-transform: uppercase;
    color: var(--accent);
  }
  .card__divider {
    width: 5px;
    background: var(--accent);
  }
  .card__info-side {
    flex: 1;
    background: var(--card-dark);
    color: var(--text-light);
    padding: 62px 20px 0 37px;
    font-family: "Lato", sans-serif;
  }
  .person-name {
    font-family: "Oswald", sans-serif;
    font-weight: 400;
    font-size: 28px;
    line-height: 34px;
    text-transform: uppercase;
    letter-spacing: 0.3px;
  }
  .person-role {
    font-size: 18px;
    line-height: 22px;
    margin-bottom: 12px;
  }
  .contact-line {
    display: flex;
    align-items: center;
    gap: 5px;
    font-size: 18px;
    line-height: 25px;
  }
  .contact-line svg { width: 16px; height: 16px; fill: var(--text-light); }
  .services {
    list-style: none;
    margin-top: 64px;
    font-size: 18px;
    line-height: 23.5px;
  }
  .services li {
    position: relative;
    padding-left: 17px;
  }
  .services li::before {
    content: "";
    position: absolute;
    left: 1px;
    top: 8px;
    width: 8px;
    height: 8px;
    border-radius: 50%;
    background: var(--text-light);
  }
</style>
</head>
<body>
<main class="canvas">
  <article class="card">
    <section class="card__brand-side">
      <span class="brand-name">Sola Brisa</span>
    </section>
    <div class="card__divider"></div>
    <section class="card__info-side">
      <h1 class="person-name">Dorvalle Ansel</h1>
      <p class="person-role">Audiologue</p>
      <p class="contact-line">
        <svg viewBox="0 0 16 16" aria-hidden="true"><path d="M1 6c0-2 3-4 7-4s7 2 7 4v1h-4V5.5C10 5 9 4.8 8 4.8S6 5 5 5.5V7H1z M3 8h10l1 6H2z M8 9.5a2 2 0 1 0 0 4 2 2 0 0 0 0-4z"/></svg>
        0481/27 53 09
      </p>
      <p class="contact-line">
        <svg viewBox="0 0 16 16" aria-hidden="true"><path d="M2 4h12v9H2z M3 5l5 4 5-4" stroke="#263a4d" stroke-width="1"/></svg>
        info@solabrisa.com
      </p>
      <ul class="services">
        <li>Solutions Auditives</li>
        <li>Protection auditives</li>
        <li>Acouphène</li>
        <li>Hyperacousie</li>
      </ul>
    </section>
  </article>
</main>
</body>
</html>
```